Harlow & Pike Business Cards

I already have an existing logo but would like business cards as a compliment. New business looking to to buy and hold residential properties and wholesale real estate properties as well. I do not have an existing tag line, but I am working on something simple to incorporate.

Target Market(s)

Homeowners looking to sell

Contact Information for Business Card

Morvina T. Harlow
harlowandpike@mailvale.net

P.O. Box 812
Lithonia, GA 30417

470.618.2093

Font styles to use
Serif

Requirements
Must have
• Tag line “ We Make Selling Easy”
Nice to have
• I’m open to all things creative
Should not have
• No black background

```html
<!DOCTYPE html>
<html lang="en">
<head>
<meta charset="UTF-8">
<title>Harlow &amp; Pike Business Cards</title>
<link rel="stylesheet" href="https://fonts.googleapis.com/css2?family=Merriweather:ital,wght@0,400;0,700;0,900;1,400&display=swap">
<style>
  :root {
    --backdrop: #3b3b3d;
    --card: #1f2b47;
    --card-front: #1c2742;
    --emboss: #8f9ab3;
    --gold: #d9a42a;
    --gold-light: #f2c652;
    --gold-dark: #b9821b;
    --navy: #1e1c5e;
    --accent: #4b47c2;
    --ink-light: #eef0f5;
    --ink-muted: #c6cbd8;
  }
  * { margin: 0; padding: 0; box-sizing: border-box; }
  html, body {
    width: 799px;
    height: 1200px;
    overflow: hidden;
    background: var(--backdrop);
    font-family: "Merriweather", serif;
  }
  .sheet { position: relative; width: 799px; height: 1200px; }
  .card {
    position: absolute;
    left: 50px;
    width: 700px;
    height: 400px;
    border-radius: 4px;
    overflow: hidden;
    box-shadow: 0 14px 30px rgba(0,0,0,0.45);
  }
  .card--front { top: 90px; background: var(--card-front); }
  .card--back { top: 690px; background: var(--card); }

  /* Front */
  .front-brand {
    position: absolute;
    inset: 0;
    display: flex;
    flex-direction: column;
    align-items: center;
    justify-content: center;
    gap: 18px;
  }
  .front-brand__row { display: flex; align-items: center; gap: 18px; }
  .front-brand__mark { width: 26px; height: 26px; background: var(--emboss); }
  .front-brand__name {
    font-weight: 900;
    font-size: 46px;
    letter-spacing: 1px;
    color: var(--emboss);
    text-transform: uppercase;
  }
  .front-brand__tagline {
    font-size: 18px;
    font-style: italic;
    letter-spacing: 1px;
    color: var(--gold);
  }

  /* Back */
  .back-brand {
    position: absolute;
    left: 36px;
    top: 110px;
    width: 300px;
    display: flex;
    flex-direction: column;
    align-items: center;
    gap: 12px;
  }
  .back-brand__mark { width: 30px; height: 30px; background: var(--gold); }
  .back-brand__name {
    font-weight: 900;
    font-size: 30px;
    color: var(--gold);
    text-transform: uppercase;
    letter-spacing: 0.5px;
    text-align: center;
    line-height: 1.15;
  }
  .back-brand__tagline {
    font-size: 14px;
    font-style: italic;
    letter-spacing: 0.5px;
    color: var(--ink-light);
  }
  .contact { position: absolute; left: 370px; top: 118px; }
  .contact__name { font-weight: 900; font-size: 24px; color: var(--gold); }
  .contact__role { margin-top: 4px; font-size: 14px; color: var(--ink-muted); }
  .contact__list { list-style: none; margin-top: 20px; display: grid; gap: 9px; }
  .contact__item {
    display: flex;
    align-items: center;
    gap: 10px;
    font-size: 15px;
    color: var(--ink-light);
    white-space: nowrap;
  }
  .contact__icon { width: 15px; height: 15px; flex: none; }
  .accent-line {
    position: absolute;
    left: 0;
    bottom: 70px;
    width: 290px;
    height: 9px;
    background: var(--accent);
  }
  .footer-band {
    position: absolute;
    right: 0;
    bottom: 0;
    width: 420px;
    height: 82px;
    border-top-left-radius: 34px;
    background: linear-gradient(100deg, var(--gold-dark), var(--gold-light) 45%, var(--gold) 100%);
    display: flex;
    align-items: center;
    padding-left: 70px;
  }
  .footer-band__text { font-weight: 700; font-size: 16px; color: var(--navy); }
</style>
</head>
<body>
<main class="sheet">
  <section class="card card--front" aria-label="Card front">
    <div class="front-brand">
      <div class="front-brand__row">
        <span class="front-brand__mark"></span>
        <span class="front-brand__name">Harlow &amp; Pike</span>
      </div>
      <p class="front-brand__tagline">We Make Selling Easy</p>
    </div>
  </section>

  <section class="card card--back" aria-label="Card back">
    <div class="back-brand">
      <span class="back-brand__mark"></span>
      <span class="back-brand__name">Harlow &amp; Pike</span>
      <p class="back-brand__tagline">We Make Selling Easy</p>
    </div>

    <div class="contact">
      <h1 class="contact__name">Morvina T. Harlow</h1>
      <p class="contact__role">Managing Director</p>
      <ul class="contact__list">
        <li class="contact__item">
          <svg class="contact__icon" viewBox="0 0 24 24"><path fill="#d9a42a" d="M6.6 10.8a15 15 0 0 0 6.6 6.6l2.2-2.2a1 1 0 0 1 1-.25 11.4 11.4 0 0 0 3.6.57 1 1 0 0 1 1 1V20a1 1 0 0 1-1 1A17 17 0 0 1 3 4a1 1 0 0 1 1-1h3.5a1 1 0 0 1 1 1c0 1.25.2 2.45.57 3.57a1 1 0 0 1-.25 1z"/></svg>
          470.618.2093
        </li>
        <li class="contact__item">
          <svg class="contact__icon" viewBox="0 0 24 24"><path fill="#d9a42a" d="M3 5h18v14H3z"/><path d="M3 5l9 8 9-8" fill="none" stroke="#1f2b47" stroke-width="1.8"/></svg>
          harlowandpike@mailvale.net
        </li>
        <li class="contact__item">
          <svg class="contact__icon" viewBox="0 0 24 24"><path fill="#d9a42a" d="M12 2a7 7 0 0 0-7 7c0 5.2 7 13 7 13s7-7.8 7-13a7 7 0 0 0-7-7zm0 9.5A2.5 2.5 0 1 1 12 6.5a2.5 2.5 0 0 1 0 5z"/></svg>
          P.O. Box 812 Lithonia, GA 30417
        </li>
      </ul>
    </div>

    <div class="accent-line"></div>
    <div class="footer-band">
      <span class="footer-band__text">Harlow &amp; Pike Holdings LLC</span>
    </div>
  </section>
</main>
</body>
</html>
```